Lumora vale- referral cards for new customers

Hey,

I would like 1 set of business cards with the following details:

10% off any sales / coupon code
Our phone number: 4702938165
Menu :Lumoravale.example (for the menu)
A line left blank to hand write an activation code: either on top or just on one side

Include the Lumora Vale logo ( your choice of black or white logo)
This card is to drive orders for people to order a cannabis order with Lumora Vale. Please make the logo a large part of the card on both sides.

Target Market(s)

People who consume cannabis 21 and up

Industry/Entity Type

Business

Contact Information for Business Card

This business card will be given to customers so they can then give it to other customers and generate referalls. We need this card to be elegant, impressionable, professional, and something worth keeping and passing to friends.

Font styles to use
Decorative
Script

Colors
33a6d7
85acd3
3176b5
0455a3
0592cd
85cae6
cee9f5
eaf1f7
757575

Requirements
Must have
• Our website
• Phone Number
• The 10% off an order
• Spot for activation code
Nice to have
• Eye catching design
• Look classy
• Textured feel or textured look
Should not have
• Do not look super cannabis heady
• Do not look attractive to children

```html
<!DOCTYPE html>
<html lang="en">
<head>
<meta charset="utf-8">
<title>Lumora Vale – Referral Cards</title>
<link rel="stylesheet" href="https://fonts.googleapis.com/css2?family=Passion+One:wght@400;700&family=Josefin+Sans:wght@400;600&display=swap">
<style>
  :root {
    --page-bg: #ecebe8;
    --card-light: #e3ebf5;
    --card-light-edge: #d4e0ee;
    --ink: #1b1b1b;
    --ink-soft: #2e2e2e;
    --card-dark: #050505;
    --ring-grey: #2a2a2a;
    --sky: #cee9f5;
    --sky-deep: #b9d6ea;
    --code-field: #eaf1f7;
    --leaf: #4f5a2a;
    --muted: #757575;
  }
  * { box-sizing: border-box; margin: 0; padding: 0; }
  html, body { width: 1200px; height: 800px; overflow: hidden; }
  body {
    background: var(--page-bg);
    font-family: "Josefin Sans", sans-serif;
    color: var(--ink);
    position: relative;
  }
  .card {
    position: absolute;
    top: 246px;
    width: 540px;
    height: 308px;
    border-radius: 4px;
    overflow: hidden;
    box-shadow: 0 6px 18px rgba(0,0,0,0.18);
  }

  /* Coupon side */
  .card--coupon {
    left: 40px;
    background:
      radial-gradient(circle at 30% 20%, rgba(255,255,255,0.55), transparent 60%),
      linear-gradient(135deg, var(--card-light) 0%, var(--card-light-edge) 100%);
  }
  .offer {
    position: absolute;
    left: 34px;
    top: 44px;
    font-family: "Passion One", sans-serif;
    line-height: 0.9;
    color: var(--ink);
  }
  .offer__amount { font-size: 58px; letter-spacing: 1px; }
  .offer__terms { font-size: 36px; letter-spacing: 1px; }
  .code-field {
    position: absolute;
    left: 40px;
    top: 152px;
    width: 234px;
    height: 56px;
    border: 2.5px solid var(--ink);
    border-radius: 10px;
    background: var(--code-field);
  }
  .contact {
    position: absolute;
    left: 40px;
    top: 238px;
    list-style: none;
    font-size: 14px;
    color: var(--ink-soft);
  }
  .contact li {
    display: flex;
    align-items: center;
    gap: 8px;
    height: 22px;
  }
  .contact svg { width: 13px; height: 13px; flex: none; }
  .coupon-mark {
    position: absolute;
    right: 56px;
    top: 22px;
    width: 200px;
    height: 188px;
    border-radius: 50%;
    background: radial-gradient(circle, #f4f4f4 0%, #9c9c9c 45%, #2f2f2f 75%, rgba(47,47,47,0) 76%);
  }
  .coupon-name {
    position: absolute;
    right: 34px;
    top: 218px;
    font-size: 34px;
    font-weight: 400;
    letter-spacing: 1px;
    color: var(--ink);
  }

  /* Logo side */
  .card--logo {
    left: 620px;
    background: var(--card-dark);
  }
  .rings {
    position: absolute;
    left: 0;
    top: 0;
    width: 540px;
    height: 308px;
  }
  .logo-mark {
    position: absolute;
    left: 185px;
    top: 32px;
    width: 190px;
    height: 190px;
    border-radius: 50%;
    background: radial-gradient(circle, #8ec7d6 0%, #6aa4b8 30%, #c0583a 48%, #4f5a2a 62%, rgba(79,90,42,0) 72%);
  }
  .logo-name {
    position: absolute;
    left: 0;
    width: 560px;
    top: 226px;
    text-align: center;
    font-size: 34px;
    font-weight: 400;
    letter-spacing: 2px;
    color: var(--ink);
  }
</style>
</head>
<body>

  <section class="card card--coupon" aria-label="Referral coupon side">
    <h1 class="offer">
      <span class="offer__amount">10% OFF</span><br>
      <span class="offer__terms">ON ANY SALES</span>
    </h1>
    <div class="code-field" aria-label="Space to hand write activation code"></div>
    <ul class="contact">
      <li>
        <svg viewBox="0 0 24 24" aria-hidden="true"><path fill="currentColor" d="M6.6 10.8a15 15 0 0 0 6.6 6.6l2.2-2.2a1 1 0 0 1 1-.25 11.4 11.4 0 0 0 3.6.57 1 1 0 0 1 1 1V20a1 1 0 0 1-1 1A17 17 0 0 1 3 4a1 1 0 0 1 1-1h3.5a1 1 0 0 1 1 1c0 1.25.2 2.45.57 3.57a1 1 0 0 1-.25 1z"/></svg>
        4702 93 8165
      </li>
      <li>
        <svg viewBox="0 0 24 24" aria-hidden="true"><circle cx="12" cy="12" r="10" fill="currentColor"/><path d="M2 12h20M12 2c3 3 3 17 0 20M12 2c-3 3-3 17 0 20" stroke="#e3ebf5" stroke-width="1.4" fill="none"/></svg>
        Lumoravale.example (for the menu)
      </li>
    </ul>
    <div class="coupon-mark" role="img" aria-label="Brand illustration in black and grey"></div>
    <p class="coupon-name">Lumora Vale</p>
  </section>

  <section class="card card--logo" aria-label="Logo side">
    <svg class="rings" viewBox="0 0 540 308" aria-hidden="true">
      <defs>
        <radialGradient id="sky-fill" cx="50%" cy="40%" r="60%">
          <stop offset="0%" stop-color="#dff1fa"/>
          <stop offset="100%" stop-color="#b9d6ea"/>
        </radialGradient>
      </defs>
      <circle cx="290" cy="150" r="186" fill="#cee9f5"/>
      <circle cx="290" cy="150" r="176" fill="#050505"/>
      <circle cx="290" cy="150" r="166" fill="#2a2a2a"/>
      <circle cx="290" cy="150" r="150" fill="url(#sky-fill)"/>
    </svg>
    <div class="logo-mark" role="img" aria-label="Brand illustration in blue, green and warm tones"></div>
    <p class="logo-name">Lumora Vale</p>
  </section>

</body>
</html>
```